Business Card Design Project - veltramo

We are building an agency for innovative solutions in marketing, education and events to pharmaceutical companies, physicians, medical societies, patient advocacy groups. We want to become a reference in this market in Brazil as the most boutique agency here. We deal with every detail with a lot of love and caring for what we do like craftsmen.
Our card must show innovation and inspiration. Yet should be clean. Something like Swiss design, quince design, etc.
Updates
Reason: I think the initial time was too short. I believe with more time you can exceed expectations. I'm liking a lot this experience
Target Market(s)
Pharmaceutical companies, doctors and patients
Industry/Entity Type
Pharmaceutical
Font styles to use
Other font styles liked:
- Helvetia family
Colors
Designer to choose colors to be used in the design.
Requirements
Must have
- Modern, clean,
Nice to have
- Innovative idea to show
Should not have
- Not too appear too much Comercial. Must be modern but sober.

```html
<!DOCTYPE html>
<html lang="en">
<head>
<meta charset="utf-8">
<title>veltramo – business cards</title>
<link rel="stylesheet" href="https://fonts.googleapis.com/css2?family=Arimo:wght@400;700&family=Quicksand:wght@500&display=swap">
<style>
  :root {
    --backdrop: #d9d9db;
    --paper: #ffffff;
    --brand-blue: #2f7fc4;
    --brand-blue-deep: #2466ae;
    --brand-green: #7cc24e;
    --ink: #1e1e1e;
    --muted: #4a4a4a;
  }
  * { margin: 0; padding: 0; box-sizing: border-box; }
  html, body { width: 1200px; height: 864px; overflow: hidden; }
  body {
    background: radial-gradient(ellipse at 40% 35%, #eeeeef 0%, var(--backdrop) 70%);
    font-family: "Arimo", Arial, sans-serif;
    position: relative;
  }
  .card {
    position: absolute;
    width: 540px;
    height: 309px;
    border-radius: 4px;
    overflow: hidden;
    box-shadow: 0 10px 30px rgba(0,0,0,0.18);
  }
  .card-front { left: 70px; top: 450px; background: var(--paper); }
  .card-front .wordmark {
    position: absolute; left: 40px; top: 34px;
    font-family: "Quicksand", "Arimo", sans-serif; font-weight: 500;
    font-size: 78px; letter-spacing: -1px; line-height: 1;
    color: var(--brand-blue);
  }
  .person { position: absolute; left: 42px; top: 126px; }
  .person-name { color: var(--brand-blue); font-size: 17px; font-weight: 400; letter-spacing: 0.3px; line-height: 1.1; }
  .person-role { color: var(--muted); font-size: 11.5px; margin-top: 1px; line-height: 1.2; }
  .contacts { position: absolute; left: 42px; top: 172px; list-style: none; }
  .contacts li {
    display: flex; align-items: center; gap: 10px;
    font-size: 14px; line-height: 1; color: var(--ink); height: 19px;
  }
  .contacts svg { width: 15px; height: 13px; flex: none; }
  .band-line { position: absolute; left: 0; right: 0; bottom: 46px; height: 6px; background: var(--brand-blue); }
  .band-green { position: absolute; left: 0; bottom: 0; width: 235px; height: 40px; background: var(--brand-green); }
  .band-blue {
    position: absolute; left: 241px; right: 0; bottom: 0; height: 40px;
    background: linear-gradient(90deg, var(--brand-blue), var(--brand-blue-deep));
  }
  .card-back {
    left: 590px; top: 90px;
    background: linear-gradient(160deg, #3d8bca 0%, var(--brand-blue) 55%, #2f78bd 100%);
  }
  .card-back .wordmark {
    position: absolute; right: 40px; bottom: 44px;
    font-family: "Quicksand", "Arimo", sans-serif; font-weight: 500;
    font-size: 72px; letter-spacing: -1px; line-height: 1;
    color: var(--paper);
  }
</style>
</head>
<body>

<section class="card card-back" aria-label="Card back">
  <div class="wordmark">veltramo</div>
</section>

<section class="card card-front" aria-label="Card front">
  <div class="wordmark">veltramo</div>

  <div class="person">
    <div class="person-name">CLARA REIS</div>
    <div class="person-role">Managing Director</div>
  </div>

  <ul class="contacts">
    <li>
      <svg viewBox="0 0 16 14" aria-hidden="true"><path d="M1 4c0-2 3-3 7-3s7 1 7 3v1h-4V3.5H5V5H1z M3 7h10l1 6H2z" fill="#2f7fc4"/></svg>
      0055 2741 830
    </li>
    <li>
      <svg viewBox="0 0 16 14" aria-hidden="true"><rect x="4" y="0.5" width="8" height="4" fill="#2f7fc4"/><rect x="1" y="5" width="14" height="6" rx="1" fill="#2f7fc4"/><rect x="4" y="9" width="8" height="4.5" fill="#fff" stroke="#2f7fc4"/></svg>
      0055 2741 831
    </li>
    <li>
      <svg viewBox="0 0 16 14" aria-hidden="true"><rect x="0.5" y="1.5" width="15" height="11" fill="#2f7fc4"/><path d="M1 2l7 6 7-6M1 12l5-5M15 12l-5-5" stroke="#fff" fill="none"/></svg>
      hello@veltramo.com
    </li>
    <li>
      <svg viewBox="0 0 16 14" aria-hidden="true"><rect x="1" y="1" width="14" height="9" fill="none" stroke="#2f7fc4" stroke-width="1.6"/><path d="M5 13h6M8 10v3" stroke="#2f7fc4" stroke-width="1.6"/></svg>
      www.veltramo.com
    </li>
  </ul>

  <div class="band-line"></div>
  <div class="band-green"></div>
  <div class="band-blue"></div>
</section>

</body>
</html>
```